依頼詳細
【 デザインイメージ 】
・主に男性向けで、高級感がある、尿酸サプリにしたいです。
・ターゲット層:50~60代の男性
・色のイメージ 黄色か・金色 + α
・商品画像をパッと見て 「高級感」「イメージしやすさ」「しっかり入っていそう」とわかりやすいもの

※本品は「機能性表示食品」です そのため恐れ入りますが、暮らし安全局からの差し戻しにより、
軽微なテキスト修正などが、半年間ほどの間に2回ほど発生する可能性があります

・詳細は添付ファイルをご参考ください。
【 依頼内容 】
・ラベル ラベルサイズ 縦110 * 横80 (白いアルミチャック袋にラベルを貼ります)

・詳細は添付ファイルをご参考ください。

▼重要視する点・経験
・サプリメント、化粧品等のパッケージデザインをした経験

▼注意点・禁止事項
※他で登録されているデザインや商標の転用など、他社の知的財産権、著作権を侵すこと
※他のクライアントへ既に提案した内容の転用など

作成して頂くパッケージのデザインについてご質問等ありましたら、お気軽にご連絡下さい。
たくさんのデザイナー・クリエイターの方々からの応募をお待ちしております!
希望イメージ
シンプル 複雑
単色 カラフル
暗い 明るい
日常 高級
遊び心 厳粛
未来的 伝統的
女性的 男性的
希望する色
青系、黄・オレンジ系、尿酸なので、黄色がイメージしやすいと思っています… 詳細は添付資料をご覧ください
納品ファイル
• 高解像度JPG (.jpg)
• イラストレーター形式 (.ai)
補足説明
■ 選んだ理由

どのご提案も弊社の希望を盛り込んで頂いておりましたが、こちらのデザイン案は、
社内で「男性票」が一番多く入り、希望したテイストに仕上がっていた点が採用の決め手になりました。

■ 提案者全員のお礼・コメント

この度は多数のご提案ありがとうございました!
機能性表示食品の「規定」もある程度ふまえて選択させていただきましたが
どのデザイン案も素敵なものばかりでした。
また機会がございましたらよろしくお願い申し上げます。

```html
<!DOCTYPE html>
<html lang="ja">
<head>
<meta charset="utf-8">
<title>尿酸ゴールドケア ラベル</title>
<link rel="stylesheet" href="https://fonts.googleapis.com/css2?family=Noto+Sans+JP:wght@400;700;900&family=Zen+Kaku+Gothic+New:wght@900&display=swap">
<style>
  :root {
    --page: #ffffff;
    --ink: #1e1a16;
    --brown: #4a2a0c;
    --red: #d4141c;
    --gold-dark: #e89a12;
    --gold-mid: #f6b628;
    --gold-light: #fde58a;
    --cream: #fff6cf;
    --panel: #ffffff;
    --panel-text: #3b3026;
  }
  * { margin: 0; padding: 0; box-sizing: border-box; }
  html, body { width: 846px; height: 1200px; overflow: hidden; background: var(--page); }
  body { font-family: "Noto Sans JP", sans-serif; color: var(--ink); }
  .label { position: relative; width: 846px; height: 1200px; background: var(--page); }

  .label-head { position: absolute; left: 0; top: 0; width: 100%; height: 160px; background: var(--page); }
  .food-class {
    position: absolute; left: 0; top: 36px; width: 100%; text-align: center;
    font-weight: 700; font-size: 26px; letter-spacing: 6px; color: var(--ink); line-height: 36px;
  }
  .brand {
    position: absolute; left: 0; top: 80px; width: 100%;
    display: flex; justify-content: center; align-items: center; gap: 14px;
  }
  .brand-square { width: 26px; height: 26px; background: var(--brown); }
  .brand-name {
    font-family: "Noto Sans JP", sans-serif; font-weight: 900; font-size: 42px;
    color: var(--brown); letter-spacing: 3px; line-height: 56px;
  }

  .label-body {
    position: absolute; left: 0; top: 160px; width: 100%; height: 1040px;
    background: linear-gradient(135deg, var(--gold-dark) 0%, var(--gold-mid) 45%, var(--gold-dark) 100%);
  }
  .claim-band {
    position: absolute; left: 0; top: 20px; width: 100%; height: 590px;
    background: linear-gradient(180deg, var(--gold-mid) 0%, var(--gold-light) 30%, var(--cream) 55%, var(--gold-light) 80%, var(--gold-mid) 100%);
  }
  .target {
    position: absolute; left: 40px; top: 40px; font-size: 54px; font-weight: 900;
    color: var(--brown); letter-spacing: 1px; line-height: 70px;
  }
  .headline {
    position: absolute; left: 36px; top: 140px; font-family: "Zen Kaku Gothic New", sans-serif;
    font-weight: 900; color: var(--red); font-size: 140px; line-height: 180px; letter-spacing: 0;
  }
  .content-box {
    position: absolute; right: 24px; top: 140px; width: 164px; padding: 8px 0;
    border: 3px solid var(--brown); background: rgba(255,255,255,0.6);
    text-align: center; color: var(--brown);
  }
  .content-box .dose { font-size: 18px; font-weight: 700; }
  .content-box .count { font-size: 54px; font-weight: 900; line-height: 62px; }
  .content-box .count small { font-size: 26px; }
  .content-box .weight { font-size: 15px; }
  .ingredient {
    position: absolute; left: 0; top: 626px; width: 100%; text-align: center;
    font-size: 50px; font-weight: 900; color: var(--brown); letter-spacing: 1px; line-height: 70px;
  }
  .notice {
    position: absolute; left: 30px; top: 730px; width: 786px; height: 420px;
    background: var(--panel); padding: 28px 30px; color: var(--panel-text);
    font-size: 24px; line-height: 40px;
  }
  .notice p + p { margin-top: 16px; }
</style>
</head>
<body>
<div class="label">
  <header class="label-head">
    <div class="food-class">機能性表示食品</div>
    <div class="brand">
      <span class="brand-square"></span>
      <span class="brand-name">尿酸ゴールドケア</span>
    </div>
  </header>
  <section class="label-body">
    <div class="claim-band"></div>
    <p class="target">尿酸値が高めな方の</p>
    <h1 class="headline">尿酸値を<br>下げる</h1>
    <div class="content-box">
      <div class="dose">1日3粒目安</div>
      <div class="count">90<small>粒</small></div>
      <div class="weight">内容量 27.0g</div>
    </div>
    <p class="ingredient">菊の花由来ルテオリン配合</p>
    <div class="notice">
      <p>届出表示：本品にはルテオリンが含まれます。ルテオリンには尿酸値が高めの方の尿酸値を下げる機能があることが報告されています。</p>
      <p>届出番号：G000 ●●●●　本品は暮らし安全局長官による個別審査を受けたものではありません。食生活は主食、主菜、副菜を基本に食事のバランスを。</p>
    </div>
  </section>
</div>
</body>
</html>
```